hotel renovation business brochure 1 page front and back

Our current brochure is dated. It has too much information hence the key messages are getting lost. Key messages: one stop shopping or turn key services for hotel renovations; cheaper and quicker to renovate. The only art work that cant be changes is the logo. Using the material in the brochure, create a more concise message to clients while still informing them of all the services we do. Need to update color scheme to match the logo. Would like to have a few examples of renovation we have done and possibly a listing of hotel brands we have worked on.

Target Market(s)

Hotel management companies, hotel investment companies, hotel owners

Industry/Entity Type

Hospitality

Requirements
Must have
• -1 page front and back
• -be able to communicate message as one stop shopping for hotel renovations, cheaper and faster
• - hotel brightway logo design must remain
• - consistent color palette that matches logo
• - hotel brands we have worked with
• -contact information
• -pictures of renovations. can use what is in brochure or other photos attached.
Should not have
• -too many words like in current brochure but needs to communicate our advantage and all the services we offer

```html
<!DOCTYPE html>
<html lang="en">
<head>
<meta charset="utf-8">
<title>Hotel Brightway – Renovation Brochure</title>
<link href="https://fonts.googleapis.com/css2?family=Oswald:wght@400;500;600;700&family=Open+Sans:wght@400;600&display=swap" rel="stylesheet">
<style>
  :root{
    --navy:#2b2b6e;
    --orange:#d98a10;
    --ink:#1c1c1c;
    --black:#111;
    --grey:#5e5e60;
    --paper:#f6f6f6;
    --stage:#c4c4c4;
    --white:#fff;
  }
  *{box-sizing:border-box;margin:0;padding:0}
  html,body{width:1200px;height:922px;overflow:hidden}
  body{background:var(--stage);font-family:'Open Sans',sans-serif;position:relative}
  .page{position:absolute;top:111px;width:540px;height:700px;overflow:hidden;background:var(--paper);box-shadow:0 6px 18px rgba(0,0,0,.25)}
  .page--front{left:40px}
  .page--back{left:620px}
  .abs{position:absolute}
  .heading{font-family:'Oswald',sans-serif;text-transform:uppercase;line-height:1}

  /* front */
  .lobby-photo{left:0;top:0;width:540px;height:440px;background:linear-gradient(90deg,#8a7452 0%,#c9b58e 25%,#9aa0a6 70%,#d6dade 100%)}
  .title-panel{left:165px;top:0;width:210px;height:300px;background:linear-gradient(180deg,rgba(20,20,20,.85),rgba(20,20,20,.6) 75%,rgba(20,20,20,0))}
  .brand-badge{left:214px;top:20px;width:112px;height:112px;border-radius:50%;background:var(--white);display:flex;flex-direction:column;align-items:center;justify-content:center;border:4px solid #ddd}
  .brand-name{font-family:'Oswald',sans-serif;font-weight:500;color:var(--navy);font-size:14px;line-height:1.15;text-align:center;letter-spacing:.5px}
  .front-title{left:165px;top:148px;width:210px;text-align:center;color:var(--white)}
  .front-title .line{font-size:22px;font-weight:500;line-height:1.05}
  .front-title .big{font-size:34px;font-weight:600;margin-top:5px;letter-spacing:1px}
  .benefits{left:0;top:0}
  .benefit{color:var(--white);text-align:center}
  .benefit h3{font-family:'Oswald',sans-serif;font-weight:500;font-size:16px;margin-bottom:6px}
  .benefit p{font-size:10px;line-height:1.5}
  .benefit--money{left:28px;top:470px;width:150px}
  .benefit--time{left:195px;top:438px;width:152px}
  .benefit--stress{left:364px;top:456px;width:150px}
  .pitch-band{left:20px;top:582px;width:500px;height:48px;border-radius:24px;background:var(--grey);color:var(--white);font-size:15px;font-weight:500;text-align:center;padding-top:6px;line-height:1.2}
  .phone-pill{height:26px;border-radius:13px;background:var(--orange);color:var(--white);font-family:'Oswald',sans-serif;font-size:17px;font-weight:500;display:flex;align-items:center;gap:6px;padding:0 16px;z-index:2}
  .page--front .phone-pill{left:140px;top:634px}
  .footer{left:10px;top:650px;width:520px;height:50px;background:linear-gradient(90deg,#0c0c0c,#2a2a2a 50%,#0c0c0c);border-radius:14px 14px 0 0;color:var(--white)}
  .footer .details{position:absolute;left:14px;top:14px;right:14px;display:flex;justify-content:space-between;font-size:10px}
  .footer .tollfree{position:absolute;left:0;right:0;top:30px;text-align:center;font-size:15px;letter-spacing:1.5px;color:#cfcfcf}
  .footer svg{vertical-align:-2px}

  /* back */
  .kicker{left:28px;top:26px;font-size:28px;font-weight:600;color:var(--orange)}
  .back-title{left:26px;top:60px;font-size:52px;font-weight:700;color:var(--ink);letter-spacing:1px}
  .tagline{left:30px;top:148px;font-size:34px;font-weight:600;color:var(--ink);line-height:1.12}
  .tagline .accent{color:var(--navy)}
  .percent-box{left:36px;top:298px;width:214px;height:92px;border-radius:34px;background:var(--orange);color:var(--white);font-size:72px;font-weight:700;text-align:center;padding-top:9px}
  .percent-note{left:262px;top:312px;font-size:28px;font-weight:500;color:var(--ink);line-height:1.05}
  .services{left:26px;top:404px;width:488px;height:112px;border-radius:32px;background:linear-gradient(180deg,#222,#050505);color:var(--white);text-align:center;padding-top:14px;font-size:20px;font-weight:500;line-height:1.4}
  .services .sep{color:var(--orange);padding:0 5px}
  .brands{left:26px;top:526px;width:488px;height:94px;border:1.5px solid #9a9a9a;border-radius:22px;background:rgba(255,255,255,.75);padding:9px 14px}
  .brands h4{font-family:'Oswald',sans-serif;font-weight:400;font-size:11px;color:var(--ink);margin-bottom:6px}
  .brand-grid{display:grid;grid-template-columns:repeat(9,1fr);gap:5px 6px}
  .brand-grid span{height:14px;border-radius:3px;background:#d7d9de}
  .brand-grid span:nth-child(3n){background:#e4dccc}
  .brand-grid span:nth-child(4n){background:#cfd6e6}
  .page--back .phone-pill{left:150px;top:626px}
  .page--back .footer{top:644px;height:56px}
  .page--back .footer .details{top:18px}
  .page--back .footer .tollfree{top:34px}
</style>
</head>
<body>

<section class="page page--front">
  <div class="abs lobby-photo" role="img" aria-label="Photo of a renovated hotel lobby with seating and a staircase"></div>
  <div class="abs title-panel"></div>

  <div class="abs brand-badge">
    <div class="brand-name">hotel brightway<br>RALEIGH</div>
  </div>

  <h1 class="abs heading front-title">
    <div class="line">Turn key services</div>
    <div class="line">for hotel</div>
    <div class="big">Renovations</div>
  </h1>

  <svg class="abs benefits" width="540" height="600" viewBox="0 0 540 600">
    <rect x="20" y="390" width="165" height="200" fill="var(--navy)"/>
    <rect x="185" y="340" width="170" height="250" fill="var(--black)"/>
    <rect x="355" y="370" width="165" height="220" fill="var(--orange)"/>
    <polygon points="100,310 165,347 165,423 100,460 35,423 35,347" fill="#fff"/>
    <polygon points="270,255 344,297 344,383 270,425 196,383 196,297" fill="#fff"/>
    <polygon points="440,305 505,342 505,418 440,455 375,418 375,342" fill="#fff"/>
    <polygon points="100,315 161,350 161,420 100,455 39,420 39,350" fill="#b88f74" role="img" aria-label="Photo of a renovated guest room with a bed"/>
    <polygon points="270,260 340,300 340,380 270,420 200,380 200,300" fill="#b6a16b" role="img" aria-label="Photo of a renovated lobby with armchairs"/>
    <polygon points="440,310 501,345 501,415 440,450 379,415 379,345" fill="#a38d6c" role="img" aria-label="Photo of a renovated lounge with a stone fireplace"/>
  </svg>

  <div class="abs benefit benefit--money">
    <h3>SAVE MONEY</h3>
    <p>Buy at the industry's best prices. Deal with just one vendor and get huge domestic and international buying power on everything.</p>
  </div>
  <div class="abs benefit benefit--time">
    <h3>SAVE TIME</h3>
    <p>We coordinate all design, purchasing, construction and installation so your entire renovation will go faster.</p>
  </div>
  <div class="abs benefit benefit--stress">
    <h3>SAVE STRESS</h3>
    <p>We manage every detail for you. There is no renovation problem we can't solve. Your project will integrate and look better from start to finish.</p>
  </div>

  <div class="abs heading pitch-band">If you're fulfilling a PIP, upgrading, or expanding a resort, you'll<br>save money and achieve more success with Hotel Brightway.</div>

  <div class="abs phone-pill">
    <svg width="13" height="13" viewBox="0 0 24 24"><path fill="none" stroke="#fff" stroke-width="2.4" d="M5 3h4l2 5-2.5 1.5a11 11 0 0 0 6 6L16 13l5 2v4a2 2 0 0 1-2 2A17 17 0 0 1 3 5a2 2 0 0 1 2-2z"/></svg>
    919-555-0148 / 919-555-0172
  </div>

  <footer class="abs footer">
    <div class="details">
      <span><svg width="9" height="11" viewBox="0 0 12 16"><path fill="var(--orange)" d="M6 0a6 6 0 0 0-6 6c0 4.5 6 10 6 10s6-5.5 6-10a6 6 0 0 0-6-6zm0 8.5A2.5 2.5 0 1 1 6 3.5a2.5 2.5 0 0 1 0 5z"/></svg> 4820 Cedar Hollow Drive, Suite 210, Raleigh NC 27615</span>
      <span><svg width="11" height="9" viewBox="0 0 16 12"><rect x="1" y="1" width="14" height="10" fill="none" stroke="#bbb" stroke-width="1.5"/><path d="M1 1l7 6 7-6" fill="none" stroke="#bbb" stroke-width="1.5"/></svg> renovate@hotelbrightway.com</span>
    </div>
    <div class="tollfree heading">Nationwide toll-free 877-555-0190</div>
  </footer>
</section>

<section class="page page--back">
  <svg class="abs" style="left:0;top:0" width="540" height="400" viewBox="0 0 540 400">
    <polygon points="478,-15 552,28 552,114 478,157 404,114 404,28" fill="#fff" stroke="#ddd" stroke-width="2"/>
    <polygon points="478,-10 548,31 548,111 478,152 408,111 408,31" fill="#8c7a5e" role="img" aria-label="Photo of a renovated guest room with a patterned bed"/>
    <polygon points="362,115 434,157 434,241 362,283 290,241 290,157" fill="#fff" stroke="#ddd" stroke-width="2"/>
    <polygon points="362,120 430,160 430,238 362,278 294,238 294,160" fill="#a88a56" role="img" aria-label="Photo of a renovated guest room with a navy headboard"/>
    <polygon points="476,200 538,236 538,308 476,344 414,308 414,236" fill="#fff" stroke="#ddd" stroke-width="2"/>
    <polygon points="476,205 534,239 534,305 476,339 418,305 418,239" fill="#9a5a48" role="img" aria-label="Photo of a renovated lounge with red chairs"/>
  </svg>

  <div class="abs heading kicker">Easy and affordable</div>
  <h2 class="abs heading back-title">Renovations</h2>
  <div class="abs heading tagline">Everything<br>you need with<br><span class="accent">just one call!</span></div>

  <div class="abs heading percent-box">100%</div>
  <div class="abs heading percent-note">Custom and<br>complete!</div>

  <div class="abs heading services">
    Planning<span class="sep">|</span>Design<span class="sep">|</span>Specification<span class="sep">|</span>FF&amp;E<span class="sep">|</span>Logistics<br>
    Construction<span class="sep">|</span>Installation<span class="sep">|</span>Warranty<br>
    Administration
  </div>

  <div class="abs brands">
    <h4>LISTING OF HOTEL BRANDS WE HAVE WORKED ON.</h4>
    <div class="brand-grid" role="img" aria-label="Badges of hotel brands worked with">
      <span></span><span></span><span></span><span></span><span></span><span></span><span></span><span></span><span></span>
      <span></span><span></span><span></span><span></span><span></span><span></span><span></span><span></span><span></span>
      <span></span><span></span><span></span><span></span><span></span><span></span><span></span><span></span><span></span>
    </div>
  </div>

  <div class="abs phone-pill">
    <svg width="13" height="13" viewBox="0 0 24 24"><path fill="none" stroke="#fff" stroke-width="2.4" d="M5 3h4l2 5-2.5 1.5a11 11 0 0 0 6 6L16 13l5 2v4a2 2 0 0 1-2 2A17 17 0 0 1 3 5a2 2 0 0 1 2-2z"/></svg>
    919-555-0148 / 919-555-0172
  </div>

  <footer class="abs footer">
    <div class="details">
      <span><svg width="9" height="11" viewBox="0 0 12 16"><path fill="var(--orange)" d="M6 0a6 6 0 0 0-6 6c0 4.5 6 10 6 10s6-5.5 6-10a6 6 0 0 0-6-6zm0 8.5A2.5 2.5 0 1 1 6 3.5a2.5 2.5 0 0 1 0 5z"/></svg> 4820 Cedar Hollow Drive, Suite 210, Raleigh NC 27615</span>
      <span><svg width="11" height="9" viewBox="0 0 16 12"><rect x="1" y="1" width="14" height="10" fill="none" stroke="#bbb" stroke-width="1.5"/><path d="M1 1l7 6 7-6" fill="none" stroke="#bbb" stroke-width="1.5"/></svg> renovate@hotelbrightway.com</span>
    </div>
    <div class="tollfree heading">Nationwide toll-free 877-555-0190</div>
  </footer>
</section>

</body>
</html>
```